Corvane Photography Business Card Design

I need a business card designed for a photography business based in Perth, Western Australia called Corvane Photography.

We specialise in wedding, event photography and portrait photography.

The business card must borrow the style of the attached logo.

The hex codes for the colours in the logo are:
#ED1D85 - Pink
#89C23E - Green
#37282F - Black

The name on the card will be:
Name: Teodric
Phone: 0417360825
Website: www.corvanephotography-example.com.au
Facebook: corvanephotography

I am open and happy to accept creative concepts.

Industry/Entity Type

Business

```html
<!DOCTYPE html>
<html lang="en">
<head>
<meta charset="utf-8">
<title>Corvane Photography — Business Card</title>
<link rel="stylesheet" href="https://fonts.googleapis.com/css2?family=Fira+Sans+Extra+Condensed:wght@400;500&display=swap">
<style>
  :root {
    --pink: #ED1D85;
    --green: #89C23E;
    --ink: #37282F;
    --paper: #FFFFFF;
    --text-font: "Fira Sans Extra Condensed", sans-serif;
  }
  html, body {
    margin: 0;
    padding: 0;
    width: 1200px;
    height: 702px;
    overflow: hidden;
    background: var(--paper);
  }
  .card {
    position: relative;
    width: 1200px;
    height: 702px;
    overflow: hidden;
    background: var(--paper);
    font-family: var(--text-font);
  }
  .band {
    position: absolute;
    left: 0;
    width: 1200px;
    display: flex;
  }
  .band--top { top: 0; height: 77px; }
  .band--bottom { top: 623px; height: 79px; }
  .band__block { height: 100%; }
  .band__block--green { background: var(--green); }
  .band__block--pink { background: var(--pink); }
  .band--top .band__block:nth-child(1) { width: 398px; }
  .band--top .band__block:nth-child(2) { width: 403px; }
  .band--top .band__block:nth-child(3) { flex: 1; }
  .band--bottom .band__block:nth-child(1) { width: 405px; }
  .band--bottom .band__block:nth-child(2) { width: 402px; }
  .band--bottom .band__block:nth-child(3) { flex: 1; }

  .identity {
    position: absolute;
    left: 0;
    top: 77px;
    width: 630px;
    height: 546px;
    background: var(--ink);
    color: var(--green);
    text-align: center;
  }
  .identity__name {
    position: absolute;
    left: 0;
    right: 0;
    top: 166px;
    margin: 0;
    font-weight: 400;
    font-size: 128px;
    line-height: 1;
    letter-spacing: 1px;
    transform: translateX(19px);
  }
  .identity__role {
    position: absolute;
    left: 0;
    right: 0;
    top: 296px;
    margin: 0;
    font-weight: 500;
    font-size: 34px;
    line-height: 1;
    transform: translateX(19px);
  }
  .contact {
    position: absolute;
    left: 0;
    right: 0;
    top: 392px;
    margin: 0;
    padding: 0;
    list-style: none;
    display: flex;
    flex-direction: column;
    align-items: center;
    gap: 12px;
    transform: translateX(19px);
  }
  .contact__item {
    display: flex;
    align-items: center;
    gap: 10px;
    font-weight: 400;
    font-size: 21px;
    line-height: 24px;
    color: var(--green);
    white-space: nowrap;
  }
  .contact__icon {
    width: 18px;
    height: 18px;
    flex: none;
  }

  .brand {
    position: absolute;
    left: 630px;
    top: 77px;
    width: 570px;
    height: 546px;
    background: var(--paper);
  }
  .brand__mark {
    position: absolute;
    left: 175px;
    top: 136px;
    width: 186px;
    height: 186px;
  }
  .brand__name {
    position: absolute;
    left: 0;
    right: 0;
    top: 352px;
    margin: 0;
    text-align: center;
    color: var(--ink);
    font-weight: 400;
    font-size: 20px;
    line-height: 1;
    letter-spacing: 17px;
    text-transform: uppercase;
    white-space: nowrap;
    transform: translateX(-18px);
  }
</style>
</head>
<body>
  <div class="card">
    <div class="band band--top">
      <div class="band__block band__block--green"></div>
      <div class="band__block band__block--pink"></div>
      <div class="band__block band__block--green"></div>
    </div>

    <section class="identity">
      <h1 class="identity__name">TEODRIC</h1>
      <p class="identity__role">Photographer</p>
      <ul class="contact">
        <li class="contact__item">
          <svg class="contact__icon" viewBox="0 0 24 24" aria-hidden="true">
            <path fill="var(--pink)" d="M6.6 10.8a15.1 15.1 0 0 0 6.6 6.6l2.2-2.2a1 1 0 0 1 1-.25 11.4 11.4 0 0 0 3.6.57 1 1 0 0 1 1 1V20a1 1 0 0 1-1 1A17 17 0 0 1 3 4a1 1 0 0 1 1-1h3.5a1 1 0 0 1 1 1c0 1.25.2 2.45.57 3.57a1 1 0 0 1-.25 1z"/>
          </svg>
          <span>0417360825</span>
        </li>
        <li class="contact__item">
          <svg class="contact__icon" viewBox="0 0 24 24" aria-hidden="true">
            <g fill="none" stroke="var(--pink)" stroke-width="2">
              <circle cx="12" cy="12" r="9"/>
              <ellipse cx="12" cy="12" rx="4" ry="9"/>
              <path d="M3 12h18"/>
            </g>
          </svg>
          <span>www.corvanephotography-example.com.au</span>
        </li>
        <li class="contact__item">
          <svg class="contact__icon" viewBox="0 0 24 24" aria-hidden="true">
            <circle cx="12" cy="12" r="8" fill="var(--pink)"/>
          </svg>
          <span>corvanephotography</span>
        </li>
      </ul>
    </section>

    <section class="brand">
      <svg class="brand__mark" viewBox="0 0 186 186" aria-hidden="true">
        <circle cx="93" cy="93" r="93" fill="var(--pink)"/>
      </svg>
      <p class="brand__name">Corvane Photography</p>
    </section>

    <div class="band band--bottom">
      <div class="band__block band__block--green"></div>
      <div class="band__block band__block--pink"></div>
      <div class="band__block band__block--green"></div>
    </div>
  </div>
</body>
</html>
```